Webdesign für Birke Werkstatt
Zielgruppe
Birke Werkstatt produziert GfK Formteile und Abdeckungen
Einzelanfertigungen • Negativ - Formenbau • Prototyping • Ur-Modellbau
Formteile • Abdeckungen • Behälter • Sonderanfertigungen • Beschichtungen
Prototypen Modellbau • Anfertigung von Negativformen • Reparaturen • Fahrzeugteile
Hauptzielgruppe ist die Luftfahrtindustrie (Abdeckungen für Triebwerke)
Durch den Prototypenbau und die Einzelanfertigungen ist die Zielgruppe nicht klar zu definieren. Es werden Einzelteile jeglicher Art aus GfK hergestellt.
Dies können auch Anbauteile für PKW, Poolbeschichtungen, Teile für Boote etc sein.
Es gibt auch Kleinserien. Beispielsweise baut Birke-Werkstatt Motorhauben für Hallo-Brenner Rasenmähertrecker aus den 70er Jahren nach, die es nicht mehr zu kaufen gibt.
Aufgabenstellung
Der Designer hat alle Freiheiten. Die Seite muss natürlich responsiv funktionieren.
Außer dem Logo gibt es keine must-haves.
Schriftart aus dem Logo: EXO 2

```html
<!DOCTYPE html>
<html lang="de">
<head>
<meta charset="utf-8">
<title>Birke Werkstatt – GfK Formteile</title>
<link href="https://fonts.googleapis.com/css2?family=Exo+2:wght@300;400;500;700;800&display=swap" rel="stylesheet">
<style>
:root{
  --blue:#1b5ea1;
  --blue-dark:#144a82;
  --navy:#0e3a68;
  --ink:#1f1f1f;
  --grey:#f1f1f1;
  --bar:#efefef;
  --orange:#f39200;
  --white:#ffffff;
}
*{margin:0;padding:0;box-sizing:border-box}
html,body{width:1200px;height:2729px;overflow:hidden}
body{font-family:"Exo 2",sans-serif;background:var(--white);color:var(--ink);position:relative}
.abs{position:absolute}

/* header */
.brand-mark{left:108px;top:70px;width:22px;height:22px;background:var(--blue)}
.brand-name{left:142px;top:56px;font-size:62px;font-weight:800;color:var(--blue);line-height:1;letter-spacing:-1px}
.brand-tagline{left:322px;top:143px;font-size:20px;font-weight:400;color:#444}
.meta-links{right:110px;top:18px;display:flex;align-items:center;gap:24px;font-size:15px;color:var(--blue)}
.flag{width:36px;height:22px;display:block}

/* nav */
.main-nav{left:0;top:180px;width:1200px;height:51px;background:var(--blue);display:flex;padding-left:303px}
.main-nav a{color:var(--white);text-decoration:none;font-size:16px;display:flex;align-items:center;padding:0 23px;position:relative;border-right:1px solid rgba(255,255,255,.12)}
.main-nav a.active{background:var(--blue-dark)}
.main-nav a.active::after{content:"";position:absolute;left:50%;bottom:-9px;margin-left:-9px;border-left:9px solid transparent;border-right:9px solid transparent;border-top:9px solid var(--blue-dark)}
.main-nav a:last-child{border-right:0}

/* hero */
.hero{left:0;top:231px;width:1200px;height:493px;background:linear-gradient(180deg,#b9cdd8 0%,#dfe7ea 45%,#c8ccca 70%,#a9adab 100%)}
.hero-caption{left:808px;top:266px;width:392px;height:111px;background:rgba(255,255,255,.88);padding:20px 33px;font-size:30px;font-weight:800;color:var(--blue);line-height:36px}
.hero-arrow{width:62px;height:63px;background:rgba(255,255,255,.55);display:flex;align-items:center;justify-content:center;top:452px}

/* about */
.section-title{width:1200px;left:0;text-align:center;font-size:30px;font-weight:800;color:var(--blue)}
.about-photo{left:108px;top:838px;width:453px;height:333px;background:linear-gradient(135deg,#2c63b8 0%,#3f7bd0 50%,#9aa3ab 100%)}
.about-text{left:108px;top:1188px;width:460px;font-size:19px;line-height:24px;color:var(--ink)}
.feature{left:643px;width:448px;height:59px;background:var(--bar);display:flex;align-items:center;padding-left:10px;gap:16px;font-size:31px;font-weight:300;color:var(--blue)}
.feature svg{width:66px;height:46px}

/* products */
.products{left:0;top:1390px;width:1200px;height:872px;background:var(--grey)}
.view-icons{left:1008px;top:1452px;display:flex;gap:10px}
.card{top:1530px;width:289px;height:504px;background:var(--white);box-shadow:0 2px 6px rgba(0,0,0,.1);text-align:center}
.card-photo{margin:12px;height:263px}
.card h3{font-size:20px;font-weight:800;color:var(--blue);line-height:24px;height:56px;padding-top:24px;box-sizing:content-box;margin-top:-12px}
.card h3.two{margin-top:-12px}
.card p{font-size:17px;line-height:21px;padding:0 16px;height:90px}
.card .btn{display:inline-block;width:102px;height:30px;line-height:30px;background:var(--orange);color:var(--white);font-weight:700;font-size:16px;box-shadow:0 3px 6px rgba(0,0,0,.18)}
.side-arrow{top:1742px;width:62px;height:61px;background:var(--white);display:flex;align-items:center;justify-content:center}

/* contact */
.contact{left:0;top:2262px;width:1200px;height:467px;background:var(--blue)}
.contact-tab{left:90px;top:2218px;width:203px;height:46px;background:var(--blue);clip-path:polygon(18px 0,100% 0,100% 100%,0 100%);color:var(--white);font-size:30px;font-weight:800;padding-left:49px;line-height:48px}
.contact-info{left:137px;top:2297px;color:var(--white);font-weight:700;font-size:20px;line-height:24px}
.contact-info .name{font-size:28px;font-weight:800;margin-bottom:18px;line-height:34px}
.contact-info .phones{margin-top:24px}
.contact-info span{display:inline-block;width:60px}
.form-title{left:512px;top:2307px;color:var(--white);font-size:27px;font-weight:800}
.field{left:490px;width:372px;background:var(--white);border:2px solid #d6e2ee;color:var(--blue);font-size:20px;padding:6px 20px}
.send{left:742px;top:2634px;width:121px;height:38px;background:var(--navy);color:var(--white);font-weight:800;font-size:20px;text-align:center;line-height:38px}
</style>
</head>
<body>

<header>
  <div class="abs brand-mark" style="left:292px;top:96px"></div>
  <div class="abs brand-name" style="left:322px;top:74px">Birke Werkstatt</div>
  <div class="abs brand-tagline">GfK Formteile | Ur-Modellbau | Prototyping</div>
  <div class="abs meta-links">
    <span>Impressum</span><span>AGB</span>
    <svg class="flag" viewBox="0 0 36 22" aria-label="Deutsch"><rect width="36" height="7.3" fill="#000"/><rect y="7.3" width="36" height="7.4" fill="#dd0000"/><rect y="14.7" width="36" height="7.3" fill="#ffce00"/></svg>
  </div>
</header>

<nav class="abs main-nav">
  <a class="active" href="#">Startseite</a>
  <a href="#">Über uns</a>
  <a href="#">Produkte &amp; Dienstleistungen</a>
  <a href="#">Kontakt</a>
</nav>

<section>
  <div class="abs hero" role="img" aria-label="Foto: Großraum-Passagierflugzeug mit gelbem Flugzeugschlepper auf dem Vorfeld"></div>
  <div class="abs hero-caption">Abdeckungen für<br>Triebwerke</div>
  <div class="abs hero-arrow" style="left:0"><svg width="20" height="30" viewBox="0 0 20 30"><path d="M16 3 4 15l12 12" fill="none" stroke="#1b5ea1" stroke-width="5"/></svg></div>
  <div class="abs hero-arrow" style="left:1138px"><svg width="20" height="30" viewBox="0 0 20 30"><path d="M4 3l12 12L4 27" fill="none" stroke="#1b5ea1" stroke-width="5"/></svg></div>
</section>

<section>
  <h2 class="abs section-title" style="top:758px">Über uns</h2>
  <div class="abs about-photo" role="img" aria-label="Foto: Triebwerk unter blauer Schutzabdeckung auf Transportgestell"></div>
  <p class="abs about-text">Wir entwickeln und fertigen geometrisch an-spruchsvolle Formteile von höchster Qualität. Die von uns konzipierten Verbundwerkstoffe mit ihren herausragenden Oberflächen- und Materialeigen-schaften bieten konstruktive Vorteile und erweit-ern die gestalterischen Möglichkeiten.</p>
  <div class="abs feature" style="top:838px">
    <svg viewBox="0 0 66 46"><path d="M4 14 18 6l12 6 10-6 22 8v8l-8 4-10 12c-3 3-7 3-9 0l-5-4-6 4c-3 2-6 0-6-3L8 28 4 26z" fill="#1b5ea1"/><path d="M26 20l12 10M22 24l10 9M18 28l8 7" stroke="#efefef" stroke-width="2.5"/></svg>
    Kundenorientiert
  </div>
  <div class="abs feature" style="top:912px">
    <svg viewBox="0 0 66 46"><path d="M8 42a25 25 0 0 1 50 0" fill="none" stroke="#1b5ea1" stroke-width="7"/><path d="M33 42 48 24" stroke="#1b5ea1" stroke-width="5" stroke-linecap="round"/><circle cx="33" cy="42" r="5" fill="#1b5ea1"/></svg>
    Leistungsstark
  </div>
</section>

<section>
  <div class="abs products"></div>
  <h2 class="abs section-title" style="top:1444px">Produkte &amp; Dienstleistungen</h2>
  <div class="abs view-icons">
    <svg width="44" height="26" viewBox="0 0 44 26"><path d="M9 4 2 13l7 9M35 4l7 9-7 9" fill="none" stroke="#1b5ea1" stroke-width="3"/><rect x="14" y="3" width="8" height="20" fill="#1b5ea1"/><rect x="22" y="3" width="6" height="20" fill="none" stroke="#1b5ea1" stroke-width="2"/></svg>
    <svg width="26" height="26" viewBox="0 0 26 26" fill="#555"><rect width="7" height="7"/><rect x="9.5" width="7" height="7"/><rect x="19" width="7" height="7"/><rect y="9.5" width="7" height="7"/><rect x="9.5" y="9.5" width="7" height="7"/><rect x="19" y="9.5" width="7" height="7"/><rect y="19" width="7" height="7"/><rect x="9.5" y="19" width="7" height="7"/><rect x="19" y="19" width="7" height="7"/></svg>
  </div>

  <article class="abs card" style="left:108px">
    <div class="card-photo" role="img" aria-label="Foto: gelber GfK-Triebwerksdeckel" style="background:linear-gradient(135deg,#e8ec2a,#c9d11c 60%,#8a8f86)"></div>
    <h3>Luftfahrt Formbauteile</h3>
    <p>Anfertigung von Triebwerkcover für jeden Triebwerktypen.</p>
    <span class="btn">Details</span>
  </article>
  <article class="abs card" style="left:455px">
    <div class="card-photo" role="img" aria-label="Foto: aufblasbare graue Sonderabdeckung in Werkhalle" style="background:linear-gradient(135deg,#b8bcbf,#dfe1e2 55%,#8d9296)"></div>
    <h3>Aufblasbare Sonderabdeckungen</h3>
    <p>Anfertigung von Triebwerkcover für jeden Triebwerktypen.</p>
    <span class="btn">Details</span>
  </article>
  <article class="abs card" style="left:801px">
    <div class="card-photo" role="img" aria-label="Foto: blaue technische Formbauteile" style="background:linear-gradient(135deg,#2d66c9,#3f7fe0 55%,#9a8a6a)"></div>
    <h3>Formbauteile</h3>
    <p>Anfertigung von technischen Formbauteilen (Einzelstück oder Kleinserien).</p>
    <span class="btn">Details</span>
  </article>

  <div class="abs side-arrow" style="left:22px"><svg width="20" height="30" viewBox="0 0 20 30"><path d="M16 3 4 15l12 12" fill="none" stroke="#1b5ea1" stroke-width="5"/></svg></div>
  <div class="abs side-arrow" style="left:1113px"><svg width="20" height="30" viewBox="0 0 20 30"><path d="M4 3l12 12L4 27" fill="none" stroke="#1b5ea1" stroke-width="5"/></svg></div>
</section>

<footer>
  <div class="abs contact"></div>
  <div class="abs contact-tab">Kontakt</div>
  <div class="abs contact-info">
    <div class="name">Birke Werkstatt</div>
    Geschäftsführer: T. Halvern<br>
    Lindenhofweg 14<br>
    31847 Erlbach
    <div class="phones">
      <span>Tel.</span>+49 555 / 010 20 30<br>
      <span>Fax.</span>+49 555 / 010 20 31
    </div>
  </div>
  <div class="abs form-title">Ihre Nachricht</div>
  <div class="abs field" style="top:2352px;height:43px">Name</div>
  <div class="abs field" style="top:2413px;height:43px">E-Mail</div>
  <div class="abs field" style="top:2474px;height:145px;padding-top:10px">Nachricht</div>
  <div class="abs send">SENDEN</div>
</footer>

</body>
</html>
```